Pinecrest Motor Lending- Free Oil Change letters

this is A Letter from my Used Car Sales & Service business. Specifically this is in a large window envelope (See Web Links) A free oil change to get this specific customer to open the envelope. The free oil change is the top have of the letter stuff in 4 1/8 x 9 open window envelope. The rest of letter is to the Fresh bankruptcy people. The coupon is to get them to open and read my offer. I had the combined ideas from the moving target link attached.
the middle of the envelope has to have a customer name address for postal delivery
I have also included our company website and our logo to be contained. This has to be in a letter program that I will mail merge a database mailer to print.

This project is for only what will be view through the large window envelope

my company website
http://www.pmlndx.com/

envelope I use
http://www.mailerpackdepot.com/sleeves/pane/wide-pane/sleeve-73915.html

Envelope Dimensions: 4 1/8 x 9 1/2
Window Dimensions: 3 x 8 (From Left Edge: 3/4 - From Bottom Edge: 1/2)

the whole point is the make this look highend to get the customer to want read the letter.. The Letter will talk about We are the Second Change Credit Expert and to come to us to buy a used car.

Reason: Looking for so more designs

Reason: narrowing the designs and making revisions

```html
<!DOCTYPE html>
<html lang="en">
<head>
<meta charset="utf-8">
<title>Pinecrest Motor Lending – Free Oil Change Window Insert</title>
<link href="https://fonts.googleapis.com/css2?family=Open+Sans:ital,wght@0,400;0,700;0,800;1,400&display=swap" rel="stylesheet">
<style>
  :root {
    --page-bg: #f2f2f2;
    --sky-top: #4d7db3;
    --sky-mid: #4a78ad;
    --sky-deep: #22508a;
    --band-red: #931d22;
    --band-red-dark: #7d161b;
    --text-white: #ffffff;
    --text-dark: #141414;
    --cloud-light: #eef2f7;
    --cloud-blue: #a9c2de;
  }
  * { margin: 0; padding: 0; box-sizing: border-box; }
  html, body {
    width: 1200px;
    height: 1000px;
    overflow: hidden;
    background: var(--page-bg);
    font-family: "Open Sans", Arial, sans-serif;
  }
  .window-insert {
    position: absolute;
    left: 40px;
    top: 291px;
    width: 1120px;
    height: 418px;
    overflow: hidden;
    background: linear-gradient(100deg, var(--sky-top) 0%, var(--sky-mid) 45%, var(--sky-deep) 100%);
  }
  .sky-scene {
    position: absolute;
    left: 339px;
    top: 178px;
    width: 713px;
    height: 240px;
    background: radial-gradient(ellipse 60% 55% at 50% 85%, var(--cloud-light) 0%, var(--cloud-blue) 45%, rgba(169,194,222,0) 100%);
  }
  .offer-band {
    position: absolute;
    left: 0;
    top: 48px;
    width: 100%;
    height: 111px;
    background: linear-gradient(180deg, var(--band-red) 0%, var(--band-red-dark) 100%);
  }
  .offer-title {
    position: absolute;
    left: 25px;
    top: 50%;
    transform: translateY(-52%);
    color: var(--text-white);
    font-weight: 800;
    font-size: 74px;
    letter-spacing: -0.5px;
    white-space: nowrap;
  }
  .brand-name {
    position: absolute;
    left: 740px;
    top: 50%;
    transform: translateY(-50%);
    width: 340px;
    color: var(--text-white);
    font-weight: 700;
    font-size: 34px;
    line-height: 1.1;
    text-align: center;
  }
  .company-address {
    position: absolute;
    left: 833px;
    top: 204px;
    color: var(--text-white);
    font-size: 18px;
  }
  .coupon-label {
    position: absolute;
    left: 27px;
    top: 175px;
    color: var(--text-dark);
    font-style: italic;
    font-size: 21px;
  }
  .recipient {
    position: absolute;
    left: 103px;
    top: 214px;
    color: var(--text-white);
    font-size: 22px;
    line-height: 29px;
    font-style: normal;
  }
</style>
</head>
<body>
  <section class="window-insert">
    <div class="sky-scene" role="img" aria-label="Photo of an open hand beneath white clouds, one cloud shaped like a small car, against blue sky"></div>

    <div class="offer-band">
      <h1 class="offer-title">FREE OIL CHANGE</h1>
      <div class="brand-name">Pinecrest Motor Lending</div>
    </div>

    <p class="company-address">company address</p>

    <p class="coupon-label">Free Oil change coupon on name:</p>
    <address class="recipient">
      John Sample<br>
      address sample 452414<br>
      city sample<br>
      2245567
    </address>
  </section>
</body>
</html>
```